Email Banner (QuillLedger)

We require an email banner for our email promotions sent to prospect clients. The banner needs to contain the wording QuillLedger and use the same colour scheme as the logos attached.

This is for B2B professional's so needs to look like a place you would come to read technology articles.

```html
<!DOCTYPE html>
<html lang="en">
<head>
<meta charset="utf-8">
<title>QuillLedger Email Banner</title>
<link href="https://fonts.googleapis.com/css2?family=Outfit:wght@700&display=swap" rel="stylesheet">
<style>
  :root {
    --board-red: #a01d23;
    --brand-red: #d22a30;
    --brand-red-deep: #bf2228;
    --accent-soft: #dc4a4f;
    --brand-navy: #1f3352;
    --paper: #ffffff;
  }
  html, body {
    margin: 0;
    padding: 0;
    width: 1200px;
    height: 538px;
    overflow: hidden;
    background: var(--board-red);
  }
  .board {
    position: relative;
    width: 1200px;
    height: 538px;
  }
  .banner {
    position: absolute;
    left: 67px;
    width: 1067px;
    height: 146px;
    background: var(--paper);
    box-shadow: 0 18px 24px rgba(70, 8, 12, 0.45);
    overflow: hidden;
  }
  .banner--plain { top: 83px; }
  .banner--accented { top: 309px; }
  .banner__art {
    position: absolute;
    inset: 0;
    width: 1067px;
    height: 146px;
  }
  .wordmark {
    position: absolute;
    left: 39px;
    top: 0;
    height: 146px;
    display: flex;
    align-items: center;
    gap: 12px;
  }
  .wordmark__dot {
    width: 24px;
    height: 24px;
    border-radius: 50%;
    background: var(--brand-red);
  }
  .wordmark__name {
    font-family: "Outfit", sans-serif;
    font-weight: 700;
    font-size: 46px;
    letter-spacing: -0.5px;
    color: var(--brand-navy);
    line-height: 1;
  }
</style>
</head>
<body>
<div class="board">

  <section class="banner banner--plain">
    <svg class="banner__art" viewBox="0 0 1067 146" aria-hidden="true">
      <polygon points="478,0 1067,0 1067,146 338,146" fill="var(--brand-red)"/>
      <polygon points="478,0 516,0 370,146 338,146" fill="var(--brand-red-deep)"/>
      <polygon points="1067,71 1067,146 995,146" fill="var(--brand-red-deep)"/>
    </svg>
    <div class="wordmark">
      <span class="wordmark__dot"></span>
      <span class="wordmark__name">QuillLedger</span>
    </div>
  </section>

  <section class="banner banner--accented">
    <svg class="banner__art" viewBox="0 0 1067 146" aria-hidden="true">
      <polygon points="478,0 1067,0 1067,146 338,146" fill="var(--brand-red)"/>
      <polygon points="478,0 516,0 370,146 338,146" fill="var(--brand-red-deep)"/>
      <polygon points="1067,71 1067,146 995,146" fill="var(--brand-red-deep)"/>
    </svg>
    <svg class="banner__art" viewBox="0 0 1067 146">
      <rect class="accent-area accent-area--lower" x="444" y="110" width="90" height="24" rx="4"
            fill="var(--accent-soft)" role="img" aria-label="Decorative dot accent area"/>
      <rect class="accent-area accent-area--upper" x="952" y="18" width="88" height="22" rx="4"
            fill="var(--accent-soft)" role="img" aria-label="Decorative ring accent area"/>
    </svg>
    <div class="wordmark">
      <span class="wordmark__dot"></span>
      <span class="wordmark__name">QuillLedger</span>
    </div>
  </section>

</div>
</body>
</html>
```